Scrap Metal Recycling

We are looking for a simple yet bold business card. We already have the logo, please see attached. Color scheme of blue, black and white or just blue and white.

```html
<!DOCTYPE html>
<html lang="en">
<head>
<meta charset="UTF-8">
<title>R.K. Alloys Inc. – Business Card</title>
<link href="https://fonts.googleapis.com/css2?family=Montserrat:wght@700&family=Open+Sans:wght@300;600;700&display=swap" rel="stylesheet">
<style>
  :root {
    --page: #ffffff;
    --navy-deep: #121a26;
    --navy-mid: #1a2840;
    --navy-glow: #1d3050;
    --teal: #13a89e;
    --teal-dark: #0f6f72;
    --slate: #3b4a55;
    --paper: #f2f3f5;
    --brand-ink: #1c2b4a;
    --white: #ffffff;
  }
  * { margin: 0; padding: 0; box-sizing: border-box; }
  html, body {
    width: 1200px; height: 900px; overflow: hidden;
    background: var(--page);
  }
  .canvas { position: relative; width: 1200px; height: 900px; }

  .card { position: absolute; left: 274.5px; width: 651px; overflow: hidden; }

  /* Front */
  .card-front {
    top: 55.5px; height: 391.5px;
    background: var(--navy-deep);
  }
  .card-front .halo {
    position: absolute; left: 107px; top: -26px;
    width: 436px; height: 436px; border-radius: 50%;
    background: radial-gradient(circle at 50% 50%, var(--navy-glow) 0%, var(--navy-mid) 70%, #17233a 100%);
  }
  .band { position: absolute; left: 0; width: 100%; }
  .band-top {
    top: 0; height: 30px;
    background: linear-gradient(90deg, var(--slate) 0%, #1f5d66 55%, var(--teal) 100%);
  }
  .band-bottom {
    bottom: 0; height: 37.5px;
    background: linear-gradient(90deg, var(--teal) 0%, #1f6f72 50%, var(--slate) 100%);
  }
  .brand-front {
    position: absolute; left: 0; right: 0; top: 176px;
    text-align: center;
    font-family: "Montserrat", sans-serif; font-weight: 700;
    font-size: 56px; letter-spacing: 1px; line-height: 1;
    color: var(--white);
  }

  /* Back */
  .card-back {
    top: 472.5px; height: 370.5px;
    background: var(--paper);
  }
  .card-back .curves { position: absolute; left: 0; top: 0; }
  .brand-back {
    position: absolute; left: 10px; width: 262px; top: 166px;
    text-align: center;
    font-family: "Montserrat", sans-serif; font-weight: 700;
    font-size: 24px; line-height: 1;
    color: var(--brand-ink);
  }
  .person {
    position: absolute; right: 98px; top: 22px; text-align: right;
    color: var(--white); font-family: "Open Sans", sans-serif;
  }
  .person-name { font-size: 27px; font-weight: 300; letter-spacing: 0.5px; line-height: 1.1; }
  .person-name strong { font-weight: 700; }
  .person-role { font-size: 15px; font-weight: 600; letter-spacing: 1px; }

  .contact {
    position: absolute; display: flex; align-items: center;
    font-family: "Open Sans", sans-serif; font-weight: 600;
    font-size: 11.5px; line-height: 1.45; color: var(--white);
  }
  .contact svg { width: 36px; height: 36px; margin-right: 12px; flex: none; }
  .contact-email { left: 336px; top: 90px; }
  .contact-phone { left: 312px; top: 152px; }
  .contact-address { left: 316px; top: 217px; }
  .contact-web { left: 327px; top: 280px; }
</style>
</head>
<body>
<main class="canvas">

  <section class="card card-front" aria-label="Business card front">
    <div class="halo"></div>
    <div class="band band-top"></div>
    <div class="band band-bottom"></div>
    <p class="brand-front">R.K. ALLOYS INC.</p>
  </section>

  <section class="card card-back" aria-label="Business card back">
    <svg class="curves" width="651" height="371" viewBox="0 0 651 371">
      <defs>
        <linearGradient id="tealSweep" x1="0" y1="0" x2="1" y2="1">
          <stop offset="0" stop-color="#1a6e74"/>
          <stop offset="0.5" stop-color="#13a89e"/>
          <stop offset="1" stop-color="#0f5e66"/>
        </linearGradient>
        <linearGradient id="navyField" x1="0" y1="0" x2="1" y2="0">
          <stop offset="0" stop-color="#1a2840"/>
          <stop offset="1" stop-color="#121a26"/>
        </linearGradient>
      </defs>
      <path d="M300 0 C250 90 250 280 300 371 L651 371 L651 0 Z" fill="url(#tealSweep)"/>
      <path d="M322 0 C278 95 278 275 322 371 L651 371 L651 0 Z" fill="#173a4c"/>
      <path d="M338 0 C298 100 298 270 340 371 L651 371 L651 0 Z" fill="url(#navyField)"/>
      <path d="M390 0 C345 110 360 270 420 371 L651 371 L651 0 Z" fill="#162238" opacity="0.6"/>
    </svg>

    <p class="brand-back">R.K. ALLOYS INC.</p>

    <div class="person">
      <p class="person-name">MARCUS <strong>HALE</strong></p>
      <p class="person-role">GENERAL MANAGER</p>
    </div>

    <div class="contact contact-email">
      <svg viewBox="0 0 36 36" aria-hidden="true"><circle cx="18" cy="18" r="17" fill="#fff"/><rect x="10" y="12" width="16" height="12" rx="1" fill="#1a2840"/><path d="M10 12 L18 19 L26 12" stroke="#fff" stroke-width="1.5" fill="none"/></svg>
      <span>INFO@COMPANYNAME.COM</span>
    </div>

    <div class="contact contact-phone">
      <svg viewBox="0 0 36 36" aria-hidden="true"><circle cx="18" cy="18" r="17" fill="#fff"/><path d="M13 10 l3 0 l1.5 4 l-2 1.5 c1 2.3 2.7 4 5 5 l1.5 -2 l4 1.5 l0 3 c0 1 -1 2 -2 2 c-7 -0.5 -12.5 -6 -13 -13 c0 -1 1 -2 2 -2 z" fill="#1a2840"/></svg>
      <span>+00 1234 5678 9012<br>+00 1234 5678 9012</span>
    </div>

    <div class="contact contact-address">
      <svg viewBox="0 0 36 36" aria-hidden="true"><circle cx="18" cy="18" r="17" fill="#fff"/><path d="M9 18 L18 10 L27 18 L24.5 18 L24.5 26 L20 26 L20 21 L16 21 L16 26 L11.5 26 L11.5 18 Z" fill="#1a2840"/></svg>
      <span>YOUR CITY ADDRESS<br>STREET LOCATION, NY CITY, USA</span>
    </div>

    <div class="contact contact-web">
      <svg viewBox="0 0 36 36" aria-hidden="true"><circle cx="18" cy="18" r="17" fill="#fff"/><circle cx="18" cy="18" r="8.5" fill="none" stroke="#1a2840" stroke-width="1.8"/><ellipse cx="18" cy="18" rx="3.5" ry="8.5" fill="none" stroke="#1a2840" stroke-width="1.5"/><line x1="9.5" y1="18" x2="26.5" y2="18" stroke="#1a2840" stroke-width="1.5"/></svg>
      <span>WWW.COMPANY-NAME.COM</span>
    </div>
  </section>

</main>
</body>
</html>
```